Dental Office Needs- Flyer Design for Same Day Crowns

We need a flyer that will explain the benefits of the same day crown from the patient prospective. Not show pictures of the machine that makes the crowns. See attached material for content. The flyer should use the practices PMS colors of Green 562 and Blue 3025. The ad should say to the patient - I want to go this office and get my crown done there.
Updates

Project Deadline Extended Reason: The difference in the time zone between USA and Europe has caused issues. Minor changes still need to be worked out. Added Thursday, July 14, 2016

Target Market(s)

Dental Patients

Industry/Entity Type

Dental

Requirements
Must have
• Call to Action
• Business Address and Business Logo
• Classic Design
• images of a Happy 50 year old Couple
• Gives the benefits of the same day crown
Should not have
• No Images of tooth figures
• No before or after pictures

```html
<!DOCTYPE html>
<html lang="en">
<head>
<meta charset="utf-8">
<title>Linden Dental Care – Same-Day Crown Flyer</title>
<link href="https://fonts.googleapis.com/css2?family=Bebas+Neue&family=Poppins:ital,wght@0,400;0,600;0,700;1,700&display=swap" rel="stylesheet">
<style>
  :root{
    --green:#10897a;
    --blue:#0b5a86;
    --ink:#1b1b1b;
    --white:#ffffff;
    --sheet-shadow:rgba(0,0,0,.28);
    --photo-light:#f1ece6;
    --photo-warm:#e6d3c2;
    --photo-cool:#d9e4ea;
  }
  *{margin:0;padding:0;box-sizing:border-box}
  html,body{width:1200px;height:1000px;overflow:hidden;background:var(--white)}
  body{position:relative;font-family:'Poppins',sans-serif;color:var(--ink)}
  .side-label{position:absolute;top:88px;font-family:'Poppins',sans-serif;font-weight:700;font-style:italic;font-size:24px;color:var(--blue);letter-spacing:.5px}
  .sheet{position:absolute;top:135px;width:548px;height:775px;background:var(--white);box-shadow:0 3px 10px var(--sheet-shadow);overflow:hidden}
  .sheet--front{left:37px}
  .sheet--back{left:620px}
  .photo{position:absolute}
  .headline{position:absolute;font-family:'Bebas Neue',sans-serif;line-height:.98;letter-spacing:.2px}
  .headline span{display:block}
  .g{color:var(--green)} .b{color:var(--blue)}
  .wave{position:absolute;left:0;width:548px}
  .brand{position:absolute;font-family:'Poppins',sans-serif;font-weight:600;color:var(--blue);white-space:nowrap}
  .brand-badge{position:absolute;left:298px;top:362px;width:214px;height:76px;border-radius:50%;background:var(--white);box-shadow:0 2px 6px rgba(0,0,0,.18);display:flex;align-items:center;justify-content:center;z-index:2}
  .brand-badge .brand{position:static;font-size:14px}
  .copy{position:absolute;font-size:10px;line-height:1.35}
  .copy p{margin-bottom:9px}
  .copy strong{font-weight:700}
  .copy .lead{font-weight:700;font-style:italic;font-size:12.5px;line-height:1.2;margin-top:14px}
  .goodbye{position:absolute;left:325px;top:458px}
  .goodbye li{list-style:none;display:flex;align-items:flex-start;margin-bottom:10px}
  .goodbye svg{width:14px;height:20px;margin:6px 8px 0 0;flex:none}
  .goodbye .big{display:block;font-family:'Bebas Neue',sans-serif;font-size:32px;line-height:.95;color:var(--green)}
  .goodbye .small{display:block;font-family:'Bebas Neue',sans-serif;font-size:16px;line-height:1;color:var(--blue)}
  .benefits{position:absolute;left:0;width:548px;top:670px;text-align:center;font-family:'Bebas Neue',sans-serif;font-size:23.5px;color:var(--green);line-height:1.3}
  .benefits span{display:inline-flex;align-items:center;margin:0 7px}
  .benefits svg{width:15px;height:13px;margin-right:5px}
  .back-intro{position:absolute;left:25px;top:226px;font-size:10.5px;line-height:1.25;width:200px}
  .back-intro p{margin-bottom:8px}
  .back-body{position:absolute;left:25px;top:446px;width:500px;font-size:10.6px;line-height:1.35;text-align:justify}
  .call{position:absolute;left:25px;top:698px;font-family:'Bebas Neue',sans-serif;font-size:30px;color:var(--blue);line-height:1}
  .address{position:absolute;left:25px;top:730px;font-weight:700;font-size:13px;color:var(--blue)}
</style>
</head>
<body>

<div class="side-label" style="left:264px">FRONT</div>
<div class="side-label" style="left:882px">BACK</div>

<!-- FRONT SIDE -->
<section class="sheet sheet--front">
  <div class="photo" role="img" aria-label="Smiling couple in their fifties, cheek to cheek"
       style="left:70px;top:0;width:478px;height:420px;background:linear-gradient(90deg,var(--white) 0%,var(--photo-light) 30%,var(--photo-warm) 70%,#d8cfc7 100%)"></div>

  <h1 class="headline" style="left:30px;top:58px;font-size:41px">
    <span class="g">Are you ready for</span>
    <span class="g">a dramatically</span>
    <span class="b">improved</span>
    <span class="g">experience</span>
    <span class="g">with your</span>
    <span class="b">next crown?</span>
  </h1>

  <svg class="wave" style="top:340px" width="548" height="120" viewBox="0 0 548 120">
    <path d="M0 18 C120 0 220 10 330 40 C420 64 490 60 548 44 L548 120 L0 120Z" fill="var(--green)"/>
    <path d="M0 40 C120 22 230 34 330 62 C420 86 490 80 548 66 L548 120 L0 120Z" fill="var(--blue)"/>
    <path d="M0 96 C140 70 260 70 380 86 C460 96 510 96 548 92 L548 120 L0 120Z" fill="var(--white)"/>
  </svg>

  <div class="brand-badge"><span class="brand">Linden Dental Care</span></div>

  <div class="copy" style="left:30px;top:466px;width:270px">
    <p><strong>LINDEN DENTAL CARE</strong> is pleased to offer you the Comfort and Convenience of One Visit Dental Care.</p>
    <p>Restorative dentistry has evolved and now, digital technology allows us to take an impression of your teeth with a digital scanner and create your restoration right in our office</p>
    <p class="lead">When it comes to your next crown, the benefits of a Digital Restoration add up quickly!</p>
  </div>

  <ul class="goodbye">
    <li><svg viewBox="0 0 14 20"><path d="M2 2 L11 10 L2 18" fill="none" stroke="var(--blue)" stroke-width="3.5"/></svg>
      <div><span class="big">Good-bye</span><span class="small">Temporary crown</span></div></li>
    <li><svg viewBox="0 0 14 20"><path d="M2 2 L11 10 L2 18" fill="none" stroke="var(--blue)" stroke-width="3.5"/></svg>
      <div><span class="big">Good-bye</span><span class="small">Second appointment</span></div></li>
    <li><svg viewBox="0 0 14 20"><path d="M2 2 L11 10 L2 18" fill="none" stroke="var(--blue)" stroke-width="3.5"/></svg>
      <div><span class="big">Good-bye</span><span class="small">Gooey messy impressions</span></div></li>
  </ul>

  <div class="benefits">
    <span><svg viewBox="0 0 15 13"><path d="M1 7 L5 11 L14 1" fill="none" stroke="var(--blue)" stroke-width="2.6"/></svg>A same-day restoration</span>
    <span><svg viewBox="0 0 15 13"><path d="M1 7 L5 11 L14 1" fill="none" stroke="var(--blue)" stroke-width="2.6"/></svg>A stronger more precise fit</span><br>
    <span><svg viewBox="0 0 15 13"><path d="M1 7 L5 11 L14 1" fill="none" stroke="var(--blue)" stroke-width="2.6"/></svg>A beautiful natural appearance</span>
  </div>

  <svg class="wave" style="top:730px" width="548" height="45" viewBox="0 0 548 45">
    <path d="M0 14 C160 2 300 2 420 16 C480 24 520 22 548 14 L548 45 L0 45Z" fill="var(--blue)"/>
  </svg>
</section>

<!-- BACK SIDE -->
<section class="sheet sheet--back">
  <div class="photo" role="img" aria-label="Happy mature couple smiling together outdoors"
       style="left:0;top:0;width:548px;height:420px;background:linear-gradient(100deg,#f3f5f2 0%,#e9eee8 35%,var(--photo-warm) 65%,var(--photo-cool) 100%)"></div>

  <h2 class="headline" style="left:25px;top:44px">
    <span class="g" style="font-size:60px">Same-day</span>
    <span class="b" style="font-size:60px">Digital</span>
    <span class="b" style="font-size:44px">Restorations.</span>
  </h2>

  <div class="back-intro">
    <p>Crowns, veneers and bridges that happen in hours instead of days.</p>
    <p>Ask your dentist if digital dentistry is right for you.</p>
  </div>

  <div class="brand" style="left:380px;top:318px;font-size:15px">Linden Dental Care</div>

  <svg class="wave" style="top:352px" width="548" height="80" viewBox="0 0 548 80">
    <path d="M0 20 C110 0 220 8 330 34 C420 54 490 56 548 48 L548 80 L0 80Z" fill="var(--green)"/>
    <path d="M0 36 C110 18 220 28 330 52 C420 70 490 72 548 64 L548 80 L0 80Z" fill="var(--blue)"/>
    <path d="M0 66 C140 50 280 62 380 76 L400 80 L0 80Z" fill="var(--white)"/>
    <path d="M380 76 C460 82 510 72 548 70 L548 80 L380 80Z" fill="var(--white)"/>
  </svg>

  <p class="back-body"><strong>Restorative dentistry</strong> has evolved and now, digital technology allows us to take an impression of your teeth with a digital scanner and create your restoration right in our office. We can match your existing teeth and provide you with a filling, veneer, crown or bridge using the most advanced non-metal composite materials giving you a beautiful smile and natural appearance.</p>

  <div class="photo" role="img" aria-label="Dentist holding up a dental X-ray beside a smiling young patient"
       style="left:210px;top:520px;width:338px;height:215px;background:linear-gradient(90deg,var(--white) 0%,#eef1f4 30%,#f1e7dc 75%,#efe0c9 100%)"></div>

  <h3 class="headline g" style="left:25px;top:536px;font-size:38px">
    <span>Find out if</span>
    <span>digital</span>
    <span>dentistry</span>
    <span>is right for you.</span>
  </h3>

  <div class="call">Call us today&nbsp; 555.014.2273</div>
  <div class="address">48 E. Maple Ave.&nbsp; Brookvale, MI 48000</div>

  <svg class="wave" style="top:730px" width="548" height="45" viewBox="0 0 548 45">
    <path d="M0 30 C160 26 300 26 420 18 C480 12 520 6 548 2 L548 45 L0 45Z" fill="var(--blue)"/>
  </svg>
</section>

</body>
</html>
```